Celebrate Weekends

Hi Mirela,

I'm looking to do another promo poster for my shop. Please use similar style as GLENDORIX poster

Title and description :

CELEBRATE WEEKEND
$10 PHO
ALL DAY SATURDAY & SUNDAY

Order your BOWL & DASH or Eat-In
Limited Time Only
...............................................................

* Must use these photos in the poster

```html
<!DOCTYPE html>
<html lang="en">
<head>
<meta charset="utf-8">
<title>Celebrate Weekend – $10 Pho</title>
<link href="https://fonts.googleapis.com/css2?family=Bebas+Neue&family=Anton&display=swap" rel="stylesheet">
<style>
  :root {
    --ink: #000000;
    --paper: #ffffff;
    --accent: #f28c1e;
    --photo-dark: #1c1c1c;
    --photo-light: #d9d6cf;
  }
  html, body {
    margin: 0;
    padding: 0;
    background: var(--ink);
    overflow: hidden;
  }
  .poster {
    position: relative;
    width: 849px;
    height: 1200px;
    background: var(--ink);
    overflow: hidden;
    font-family: "Bebas Neue", "Anton", sans-serif;
  }
  .frame {
    position: absolute;
    left: 70px;
    width: 320px;
    box-sizing: border-box;
    border: 6px solid var(--paper);
  }
  .brand-box {
    top: 76px;
    height: 310px;
    background: var(--ink);
    display: flex;
    align-items: center;
    justify-content: center;
    gap: 14px;
  }
  .brand-dot {
    width: 22px;
    height: 22px;
    border-radius: 50%;
    background: var(--accent);
  }
  .brand-name {
    color: var(--accent);
    font-size: 58px;
    letter-spacing: 2px;
    line-height: 1;
  }
  .dish {
    height: 219px;
    background: radial-gradient(ellipse at 50% 55%, var(--photo-light) 0%, #8f8a7e 32%, var(--photo-dark) 62%, #0d0d0d 100%);
  }
  .dish-chicken { top: 414px; }
  .dish-tofu { top: 662px; background: radial-gradient(ellipse at 50% 55%, #e3a86b 0%, #c9703a 22%, #e6e3dc 40%, var(--photo-dark) 64%, #0d0d0d 100%); }
  .dish-meatball { top: 909px; }

  .copy {
    position: absolute;
    left: 418px;
    margin: 0;
    white-space: nowrap;
    line-height: 1;
    font-weight: 400;
    transform-origin: left top;
  }
  .headline { color: var(--accent); font-size: 118px; }
  .headline-1 { top: 66px; transform: scaleX(0.915); }
  .headline-2 { top: 153px; transform: scaleX(1.06); }
  .price {
    color: var(--paper);
    font-size: 268px;
    top: 240px;
    left: 424px;
    -webkit-text-stroke: 5px var(--paper);
    transform: scaleX(1.13);
  }
  .dish-name { color: var(--paper); font-size: 315px; top: 484px; transform: scaleX(1); }
  .rule {
    position: absolute;
    left: 418px;
    width: 358px;
    border-top: 2px dotted var(--paper);
  }
  .rule-top { top: 756px; }
  .rule-bottom { top: 806px; }
  .schedule { color: var(--accent); font-size: 43px; top: 764px; transform: scaleX(0.965); }
  .order { color: var(--paper); font-size: 96px; }
  .order-1 { top: 819px; transform: scaleX(0.99); }
  .order-2 { top: 903px; transform: scaleX(0.92); }
  .order-3 { top: 998px; font-family: "Anton", sans-serif; font-size: 62px; line-height: 1.1; transform: scaleX(1.2); }
  .limited {
    position: absolute;
    left: 421px;
    top: 1068px;
    width: 351px;
    height: 60px;
    background: var(--accent);
    color: var(--ink);
    font-size: 58px;
    line-height: 64px;
    text-align: center;
    margin: 0;
  }
</style>
</head>
<body>
<main class="poster">
  <div class="frame brand-box">
    <span class="brand-dot"></span>
    <span class="brand-name">BOWL &amp; DASH</span>
  </div>
  <div class="frame dish dish-chicken" role="img" aria-label="Photo of a bowl of chicken pho with herbs, onion and bean sprouts"></div>
  <div class="frame dish dish-tofu" role="img" aria-label="Photo of a bowl of spicy noodle soup with fried tofu and carrot"></div>
  <div class="frame dish dish-meatball" role="img" aria-label="Photo of a bowl of beef meatball pho with onion and herbs"></div>

  <h1 class="copy headline headline-1">CELEBRATE</h1>
  <p class="copy headline headline-2">WEEKEND</p>
  <p class="copy price">$10</p>
  <p class="copy dish-name">PHO</p>

  <div class="rule rule-top"></div>
  <p class="copy schedule">ALL DAY SATURDAY &amp; SUNDAY</p>
  <div class="rule rule-bottom"></div>

  <p class="copy order order-1">ORDER YOUR</p>
  <p class="copy order order-2">BOWL &amp; DASH</p>
  <p class="copy order order-3">GO OR EAT-IN</p>

  <p class="limited">LIMITED TIME ONLY</p>
</main>
</body>
</html>
```